Business Card and Stationary Design

After the successful redesign of our logo we are wanting to follow suite and create a new business card and stationary design!

New Logo is attached, information required on the business card should contain a mixture of the following but layout/arrangement is up to the designer.

Happy if the national provider number and abn are on the back, and happy for them to be smaller than the rest.

I am also happy to receive single sided or weird and wonderful designs.

Name
Title
National Provider Number 7291
ABN 53 219 864 317
Level 3, 42 Marlow Street
Kelvin Grove NSW 2294
Ph: 1300 987 214
Mobile: 0432 785 619
name@ferngatebuild.com.au
www.ferngatebuild.com.au

Target Market(s)

Professionals, Peers, Students, Suppliers...

Industry/Entity Type

Construction

Contact Information for Business Card

Listed in project description

Font styles to use
Other font styles liked:
• Century Gothic

Colors
0455a3
3176b5
ffffff

Requirements
Must have
• Professional Design, same color scheme as our logo
Nice to have
• Something that sets our apart from everyone else would be fantastic, open to size and shape and layout options, as long as they present professionally.
• Open to raised/embossed text, alternative materials, custom sizes, clear material
Should not have
• The color orange

```html
<!DOCTYPE html>
<html lang="en">
<head>
<meta charset="utf-8">
<title>Ferngate Build — Stationery</title>
<link rel="stylesheet" href="https://fonts.googleapis.com/css2?family=Questrial&family=Open+Sans:wght@400;600&display=swap">
<style>
  :root {
    --navy: #1f3a7c;
    --blue: #0455a3;
    --accent: #3176b5;
    --paper: #ffffff;
    --ink: #2a3550;
    --muted: #5a6478;
    --backdrop: #d9dde3;
    --shadow: rgba(30, 40, 60, 0.18);
  }
  * { box-sizing: border-box; margin: 0; padding: 0; }
  html, body { width: 1200px; height: 862px; overflow: hidden; }
  body {
    background: var(--backdrop);
    font-family: "Open Sans", Arial, sans-serif;
    color: var(--ink);
    position: relative;
  }
  .sheet {
    position: absolute;
    background: var(--paper);
    box-shadow: 0 6px 18px var(--shadow);
    overflow: hidden;
  }
  .sheet-art { position: absolute; inset: 0; width: 100%; height: 100%; }
  .wordmark {
    position: absolute;
    font-family: "Questrial", "Century Gothic", sans-serif;
    color: var(--navy);
    font-weight: 400;
    letter-spacing: 0.2px;
    display: flex;
    align-items: center;
    gap: 7px;
    white-space: nowrap;
  }
  .wordmark-dot { background: var(--blue); display: inline-block; }

  /* Envelope */
  .envelope { left: 60px; top: 100px; width: 560px; height: 280px; }
  .envelope .wordmark { left: 34px; top: 120px; font-size: 24px; }
  .envelope .wordmark-dot { width: 12px; height: 12px; }
  .envelope-address {
    position: absolute; left: 34px; top: 156px;
    font-size: 10px; color: var(--ink);
  }

  /* Business cards */
  .card { top: 480px; width: 300px; height: 171px; }
  .card-front { left: 60px; }
  .card-front .wordmark { left: 50%; top: 50%; transform: translate(-50%, -50%); font-size: 24px; }
  .card-front .wordmark-dot { width: 12px; height: 12px; }
  .card-back { left: 380px; }
  .card-back .wordmark { left: 20px; top: 58px; font-size: 15px; }
  .card-back .wordmark-dot { width: 8px; height: 8px; }
  .card-person { position: absolute; right: 18px; top: 14px; text-align: right; color: var(--paper); }
  .card-name { font-size: 12px; font-weight: 600; }
  .card-title { font-size: 9px; }
  .card-contacts { position: absolute; left: 138px; top: 62px; font-size: 7.5px; line-height: 12px; }
  .card-legal { position: absolute; left: 20px; top: 86px; font-size: 6.5px; line-height: 10px; color: var(--muted); }

  /* Letterhead */
  .letterhead { left: 720px; top: 134px; width: 420px; height: 594px; }
  .letterhead .wordmark { right: 26px; top: 56px; font-size: 28px; }
  .letterhead .wordmark-dot { width: 14px; height: 14px; }
  .letterhead-contacts {
    position: absolute; left: 28px; bottom: 96px;
    font-size: 8.5px; line-height: 13px;
  }
  .letterhead-legal { font-size: 7.5px; color: var(--muted); margin-top: 3px; }

  .contact-list { list-style: none; }
  .contact-item { display: flex; align-items: center; gap: 6px; white-space: nowrap; }
  .contact-icon { width: 8px; height: 8px; flex: none; fill: var(--navy); }
</style>
</head>
<body>

<svg width="0" height="0" style="position:absolute" aria-hidden="true">
  <defs>
    <symbol id="icon-phone" viewBox="0 0 10 10"><path d="M2 0.5 3.6 0.5 4.2 3 3.2 3.8C3.8 5.2 4.8 6.2 6.2 6.8L7 5.8 9.5 6.4 9.5 8C9.5 9 8.8 9.5 8 9.5 4 9.2 0.8 6 0.5 2 0.5 1.2 1 0.5 2 0.5Z"/></symbol>
    <symbol id="icon-mobile" viewBox="0 0 10 10"><path d="M2.5 0h5a1 1 0 0 1 1 1v8a1 1 0 0 1-1 1h-5a1 1 0 0 1-1-1V1a1 1 0 0 1 1-1Zm0 1.5v6h5v-6Z"/></symbol>
    <symbol id="icon-pin" viewBox="0 0 10 10"><path d="M5 0a3.5 3.5 0 0 1 3.5 3.5C8.5 6 5 10 5 10S1.5 6 1.5 3.5A3.5 3.5 0 0 1 5 0Zm0 2a1.5 1.5 0 1 0 0 3 1.5 1.5 0 0 0 0-3Z"/></symbol>
    <symbol id="icon-mail" viewBox="0 0 10 10"><path d="M0 2h10v6H0Zm1 1v.3L5 6l4-2.7V3L5 5.6Z"/></symbol>
    <symbol id="icon-web" viewBox="0 0 10 10"><path d="M5 0a5 5 0 1 1 0 10A5 5 0 0 1 5 0Zm0 1C4.3 1.8 3.9 3 3.8 4.5h2.4C6.1 3 5.7 1.8 5 1Zm-1.2 4.5C3.9 7 4.3 8.2 5 9c.7-.8 1.1-2 1.2-3.5Z"/></symbol>
  </defs>
</svg>

<section class="sheet envelope" aria-label="DL envelope">
  <svg class="sheet-art" viewBox="0 0 560 280" preserveAspectRatio="none" aria-hidden="true">
    <path d="M380 0H560V120C520 50 460 12 380 0Z" fill="var(--navy)"/>
  </svg>
  <div class="wordmark"><span class="wordmark-dot"></span>ferngatebuild</div>
  <p class="envelope-address">Level 3, 42 Marlow Street Kelvin Grove NSW 2294</p>
</section>

<section class="sheet card card-front" aria-label="Business card front">
  <div class="wordmark"><span class="wordmark-dot"></span>ferngatebuild</div>
</section>

<section class="sheet card card-back" aria-label="Business card back">
  <svg class="sheet-art" viewBox="0 0 300 171" preserveAspectRatio="none" aria-hidden="true">
    <path d="M0 0H300V48C220 34 120 40 0 62Z" fill="var(--navy)"/>
    <path d="M190 171H300V140C260 158 225 166 190 171Z" fill="var(--navy)"/>
  </svg>
  <div class="card-person">
    <p class="card-name">Name</p>
    <p class="card-title">Title</p>
  </div>
  <div class="wordmark"><span class="wordmark-dot"></span>ferngatebuild</div>
  <ul class="contact-list card-contacts">
    <li class="contact-item"><svg class="contact-icon"><use href="#icon-phone"/></svg>Ph: 1300 987 214</li>
    <li class="contact-item"><svg class="contact-icon"><use href="#icon-mobile"/></svg>Mobile: 0432 785 619</li>
    <li class="contact-item"><svg class="contact-icon"><use href="#icon-pin"/></svg>Level 3, 42 Marlow Street</li>
    <li class="contact-item"><svg class="contact-icon"><use href="#icon-pin" opacity="0"/></svg>Kelvin Grove NSW 2294</li>
    <li class="contact-item"><svg class="contact-icon"><use href="#icon-mail"/></svg>name@ferngatebuild.com.au</li>
    <li class="contact-item"><svg class="contact-icon"><use href="#icon-web"/></svg>www.ferngatebuild.com.au</li>
  </ul>
  <div class="card-legal">
    <p>ABN 53 219 864 317</p>
    <p>National Provider Number 7291</p>
  </div>
</section>

<section class="sheet letterhead" aria-label="Letterhead">
  <svg class="sheet-art" viewBox="0 0 420 594" preserveAspectRatio="none" aria-hidden="true">
    <path d="M250 0H420V60C370 22 310 4 250 0Z" fill="var(--navy)"/>
    <path d="M0 470C60 540 150 574 260 594H0Z" fill="var(--navy)"/>
  </svg>
  <div class="wordmark"><span class="wordmark-dot"></span>ferngatebuild</div>
  <div class="letterhead-contacts">
    <ul class="contact-list">
      <li class="contact-item"><svg class="contact-icon"><use href="#icon-phone"/></svg>Ph: 1300 987 214</li>
      <li class="contact-item"><svg class="contact-icon"><use href="#icon-mobile"/></svg>Mobile: 0432 785 619</li>
      <li class="contact-item"><svg class="contact-icon"><use href="#icon-pin"/></svg>Level 3, 42 Marlow Street Kelvin Grove NSW 2294</li>
      <li class="contact-item"><svg class="contact-icon"><use href="#icon-mail"/></svg>name@ferngatebuild.com.au</li>
      <li class="contact-item"><svg class="contact-icon"><use href="#icon-web"/></svg>www.ferngatebuild.com.au</li>
    </ul>
    <p class="letterhead-legal">ABN 53 219 864 317</p>
    <p class="letterhead-legal">National Provider Number 7291</p>
  </div>
</section>

</body>
</html>
```